Corporate Design für Softwarefirma
Fantastische (!) Zusammenarbeit!! Reibungslose und schnelle Kommunikation. Änderungswünsche werden sofort entgegengenommen und umgesetzt. Soweit etwas nicht passt, wird so lange weiterverändert, bis es passt. Einfach super. Nachfragen werden binnen kürzester Zeit beantwortet - auch für allgemeine Fragen ein super Ansprechpartner. Danke hierfür ! Auch nach Ablauf des Projektes ist der Designer jederzeit ansprechbar und gibt gerne Hilfestellung. So stellt man sich Service vor! Ich kann KL47 wärmstens empfehlen. Jederzeit wieder. Die Rundum-Leistung ist klasse und das Endprodukt ohnehin super ! Nochmal herzlichen Dank!
Zielgruppe
Derzeit befinde ich mich in der Gründungsphase einer Softwarefirma namens 'BramWerk-Systems'. Nach der Namensfindung wird nun ein Corporate-Design benötig, bestehend aus einem ansprechendem Logo mit Wiedererkennungswert, einem Briefpapier für Korrespondenz und Rechnungen, sowie einer Visitenkarte inkl. QR-Code.
Tätigkeit:
Software- und Datenbankentwicklung für Firmenkunden
Zielgruppen:
sämtliche Firmen, die individuelle Softwarelösungen suchen
Was sind wir - folgende Merkmale sollen mit dem Logo visualisiert werden.
engagiert
- weil die Interessen der Kunden immer im Fokus der Zusammenarbeit stehen.
kompetent
- weil wir über hohes fachliches Know-How verfügen.
flexibel
- weil die BramWerk-Systems durch ein kleines, professionelles Team auf veränderte
Situationen sofort reagieren kann.
qualitätsbewusst
- weil die BramWerk-Systems keine Kompromisse macht wenn es um die Beratung und
Betreuung ihrer Kunden geht.
verlässlich
- weil langfristige und vertrauensvolle Beziehungen zu Geschäftspartnern zu den Grundprinzipiens unseres Handelns gehört.
unkonventionell und individuell
- weil die BramWerk-Systems immer bereit ist, im Interesse ihrer Kunden zu handeln
und unkonventionelle nicht zwingend branchentypische Lösungen zu schaffen.
Aufgabenstellung
Das Design soll klar strukturiert, modern und professionell sein. Kommuniziert werden sollen Vertrauen, Kompetenz, partnerschaftliche Zusammenarbeit, Individualität und Verlässlichkeit.
Bestehend aus einem ansprechendem Logo mit Wiedererkennungswert, einem Briefpapier für Korrespondenz und Rechnungen, sowie einer Visitenkarte inkl. QR-Code.

```html
<!DOCTYPE html>
<html lang="de">
<head>
<meta charset="utf-8">
<title>BramWerk Systems – Geschäftsausstattung</title>
<link href="https://fonts.googleapis.com/css2?family=Quicksand:wght@500;600;700&family=Open+Sans:wght@400;600;700&display=swap" rel="stylesheet">
<style>
  :root{
    --green:#a6c43a;
    --slate:#3d4350;
    --ink:#2a2c31;
    --paper:#ffffff;
    --backdrop:#2e2f33;
  }
  *{margin:0;padding:0;box-sizing:border-box}
  html,body{width:1200px;height:856px;overflow:hidden;background:var(--backdrop)}
  .stage{position:relative;width:1200px;height:856px}
  .sheet,.card{position:absolute;background:var(--paper);box-shadow:0 6px 14px rgba(0,0,0,.35)}
  .abs{position:absolute}

  /* Letterhead */
  .sheet{left:176px;top:133px;width:416px;height:588px;font-family:"Open Sans",sans-serif;color:var(--ink)}
  .sheet-band{left:0;top:0;width:8px;height:100%;background:var(--green)}
  .brand{display:flex;flex-direction:column;align-items:center;text-align:center}
  .brand-square{background:var(--green);border-radius:3px}
  .brand-name{font-family:"Quicksand",sans-serif;font-weight:600;color:var(--slate);white-space:nowrap;line-height:1.05}
  .sheet .brand{left:290px;top:34px;width:100px}
  .sheet .brand-square{width:30px;height:30px;margin-bottom:8px}
  .sheet .brand-name{font-size:12px}
  .sender-line{left:45px;top:88px;font-size:4px;font-weight:700;border-bottom:.5px solid var(--ink);padding-bottom:1px}
  .recipient{left:45px;top:108px;font-size:6.3px;line-height:8px}
  .recipient .city{margin-top:8px}
  .subject{left:45px;top:201px;font-size:6.3px;font-weight:700}
  .body-copy{left:45px;top:223px;width:228px;font-size:6.1px;line-height:7.55px}
  .body-copy p+p{margin-top:7.5px}
  .closing{left:45px;top:420px;font-size:6.1px}
  .signature{left:45px;top:436px;width:86px;height:18px;background:linear-gradient(90deg,#d9dadd,#eceded)}
  .signer{left:45px;top:461px;font-size:6.1px}
  .footer-rule{left:84px;top:538px;width:255px;height:1px;background:#8a8c90}
  .footer-col{top:547px;width:90px;text-align:center;font-family:"Quicksand",sans-serif;font-weight:600;font-size:4.3px;line-height:7px;letter-spacing:.2px}
  .footer-col svg{width:5px;height:5px;vertical-align:-1px;margin-right:1px}

  /* Business cards */
  .card{width:252px;height:163px;font-family:"Quicksand",sans-serif;color:var(--ink)}
  .card-front{left:771px;top:221px}
  .card-back{left:770px;top:471px}
  .card-front .brand{left:0;top:24px;width:100%}
  .card-front .brand-square{width:32px;height:32px;margin-bottom:10px}
  .card-front .brand-name{font-size:13px}
  .card-back .brand{left:0;top:46px;width:100%}
  .card-back .brand-square{width:40px;height:40px;margin-bottom:12px}
  .card-back .brand-name{font-size:15.5px}
  .card-line{left:0;width:100%;text-align:center;font-weight:600;font-size:5.6px;letter-spacing:.3px;white-space:nowrap}
  .card-line svg{width:7px;height:7px;vertical-align:-1.5px;margin-right:2px}
  .card-line .gap{display:inline-block;width:8px}
  .role{color:var(--green);margin-left:3px}
  .dot{color:var(--green);margin:0 3px}
  .web{color:var(--green);letter-spacing:.8px}
  .icon path,.icon rect,.icon circle{fill:none;stroke:var(--green);stroke-width:1.4}
</style>
</head>
<body>
<main class="stage">

  <section class="sheet" aria-label="Briefpapier">
    <div class="abs sheet-band"></div>
    <div class="abs brand">
      <div class="brand-square"></div>
      <div class="brand-name">BramWerk Systems</div>
    </div>
    <div class="abs sender-line">Vorname Nachname, Beispielweg 12, 12345 Probestadt</div>
    <div class="abs recipient">
      <div>Lena Probst</div>
      <div>Probeweg 45</div>
      <div class="city">12345 Berlin</div>
    </div>
    <div class="abs subject">Quidero molore, atatur sae. Nequat,</div>
    <div class="abs body-copy">
      <p>Ur sit, imus, ipicatem voluptate eum re dolluptios sequosam, eum reritati am volor sapedissi quo blaboribust, sequass itasped igendi cus exerfer feruptas iusanda ndaest, qui omnis nus aut fugitinis quatur ad ullaut mostem quasperiae corem et aciatem illatin ciduntores quidis utemquam autemperae soluptiae lab illacescia solorum et fugiam ratatatus exerro blaciis samusam etur? Uga. Neque nam simi, nest, ommod essedios magnatia nossi aute nonsequam fugiaspis moluptas sed el int etur saepe nonsecatem excea noneceperrum ulligendit faccullores et lantur si ium at.Ota cuptae non ea de opta voles rem rae dolore ilia vellab isi blanis idit veribus auda alit labore desenis imenis que in con rehent, explat ped que volorum, autent, si tetur?</p>
      <p>Ihil ium restior ecepero reptistius es aborepe diatiunt dignis diciae voluptu ribearit, que nat aute et as maximus, qui blab iur aut volest, nonsequae odios doluptatiae velignimin perescia vent. Pa voluptas expero corectur molest eaquid enda vidus verciis quodi te dit aliquid unturem poreper feratur? Quis aut rehenihilit et quam, eris et perorru mquamusa quo et untia volupie nisimoluptae esseribus cora doluptati doluptatur atisciumqui re pa quat aut lam solescia intis et millabor sit odis et quos re sam, vendicientur abo. Equi totatus rest, nosam quodi omni doloriosam des ea nimpelique volo elendae dellign ihilitis solupta temporp orupta iuntia ipiste natibusapis volesedis reriori taerrup tatiberes nobitiur, sequi omnihillab id maximagnat omnimus dolo quunt, int aut earum lacit peliquunt iduciet, id que autemolum deruptati te non re.</p>
    </div>
    <div class="abs closing">Sincerely</div>
    <div class="abs signature" role="img" aria-label="Handschriftliche Unterschrift"></div>
    <div class="abs signer">Jonas Beispiel</div>
    <div class="abs footer-rule"></div>
    <div class="abs footer-col" style="left:72px">
      Vorname Nachname<br>
      <svg class="icon" viewBox="0 0 10 10"><rect x="1" y="1" width="8" height="8" rx="1.5"/></svg>Beispielweg 12<br>
      12345 Probestadt
    </div>
    <div class="abs footer-col" style="left:168px">
      <svg class="icon" viewBox="0 0 10 10"><rect x="1" y="1" width="8" height="8" rx="1.5"/></svg>030 - 555 018 40<br>
      <svg class="icon" viewBox="0 0 10 10"><rect x="1" y="2" width="8" height="6"/><path d="M1 2l4 3.5L9 2"/></svg>info@probeseite.de<br>
      www.probeseite.de
    </div>
    <div class="abs footer-col" style="left:264px">
      Probebank gmbh<br>
      IBAN: DE00555018407<br>
      BIC: PRB000XX00
    </div>
  </section>

  <section class="card card-front" aria-label="Visitenkarte Vorderseite">
    <div class="abs brand">
      <div class="brand-square"></div>
      <div class="brand-name">BramWerk Systems</div>
    </div>
    <div class="abs card-line" style="top:99px">Name Vorname<span class="role">Geschäftsführer</span></div>
    <div class="abs card-line" style="top:113px">
      <svg class="icon" viewBox="0 0 10 10"><rect x="1" y="1" width="8" height="8" rx="1.5"/><circle cx="5" cy="4.5" r="1.5"/></svg>Beispielweg 12<span class="dot">•</span>12345 Probestadt
    </div>
    <div class="abs card-line" style="top:122px">
      <svg class="icon" viewBox="0 0 10 10"><rect x="1" y="2" width="8" height="6"/><path d="M1 2l4 3.5L9 2"/></svg>info@probeseite.de<span class="gap"></span><svg class="icon" viewBox="0 0 10 10"><rect x="1" y="1" width="8" height="8" rx="1.5"/><path d="M3.5 3c0 2 1.5 3.5 3.5 3.5"/></svg>+49 (0) 30 - 555 018-4
    </div>
    <div class="abs card-line web" style="top:137px">www.probeseite.de</div>
  </section>

  <section class="card card-back" aria-label="Visitenkarte Rückseite">
    <div class="abs brand">
      <div class="brand-square"></div>
      <div class="brand-name">BramWerk Systems</div>
    </div>
  </section>

</main>
</body>
</html>
```